Startup online payment business - Sporting / Golf, Swift Tee payment

Background:
Our business name is "Swift Tee" we provide online payments for golfing services via our website. We currently have a logo used on our website. No other design style has been developed. Our aim is to remove cash payments for service at golf clubs.

Our Key Values:
Quick and easy
Formal and polite
Fun with professional boundary
Mate-ship relationships
100% online digital

What we want from you:
Marketing design to be used on posters and stickers in a retail setting to direct customers to our online payment Chanel.
Design must incorporate attached logo, URL swifttee.com.au and our key values can act as a guide the type of design. We have used color Hex#007672 for logo background. We are open to use other colors.

Target Market(s)

Golf clubs and golf players

Industry/Entity Type

Golf Course

Font styles to use
Sans Serif

Requirements
Must have
• Directions to online payment via URL: swifttee.com.au
Nice to have
• We like the idea of the slogan: No Cash - No worries. Have attached home screen that will be available from URL link. Consideration if using mobile phone in image. Push the online payment and steps 1. Visit swifttee.com 2. Select club 3. Confirm payment
Should not have
• Cartoons

```html
<!DOCTYPE html>
<html lang="en">
<head>
<meta charset="utf-8">
<title>Swift Tee – No Cash No Worries</title>
<link href="https://fonts.googleapis.com/css2?family=Lato:wght@300;400;700;900&display=swap" rel="stylesheet">
<style>
  :root{
    --teal:#007672;
    --teal-deep:#004d4a;
    --teal-dark:#013a38;
    --teal-light:#37c4bc;
    --aqua:#7ff2ea;
    --white:#ffffff;
    --lime:#8cc63f;
    --ink:#111111;
  }
  *{margin:0;padding:0;box-sizing:border-box}
  html,body{width:1072px;height:1200px;overflow:hidden;background:var(--teal-dark)}
  .poster{
    position:relative;width:1072px;height:1200px;overflow:hidden;
    font-family:"Lato",sans-serif;color:var(--white);
    background:
      radial-gradient(ellipse 60% 12% at 50% 66%, rgba(127,242,234,.45), rgba(127,242,234,0) 70%),
      linear-gradient(180deg,var(--teal) 0%,var(--teal) 38%,#03625f 58%,var(--teal-deep) 72%,#035a57 88%,var(--teal) 100%);
  }
  .rays{position:absolute;left:0;top:560px;width:1072px;height:260px}
  .brand-name{position:absolute;top:50px;left:0;width:100%;text-align:center;
    font-weight:700;font-size:84px;letter-spacing:.06em;line-height:84px;padding-left:.06em}
  .brand-rule{position:absolute;top:139px;left:372px;width:328px;height:2px;
    background:linear-gradient(90deg,rgba(255,255,255,0),var(--white) 20%,var(--white) 80%,rgba(255,255,255,0))}
  .brand-sub{position:absolute;top:155px;left:0;width:100%;text-align:center;
    font-weight:700;font-size:24px;letter-spacing:.45em;line-height:26px;padding-left:.45em}
  .values-banner{position:absolute;left:215px;top:212px;width:642px;height:81px;
    background:linear-gradient(90deg,rgba(127,242,234,.35),rgba(127,242,234,.15) 50%,rgba(127,242,234,.45));
    border-bottom:3px solid var(--aqua);display:flex;align-items:center;justify-content:center;
    font-size:50px;font-weight:300;letter-spacing:.01em;line-height:1}
  .values-banner b{font-weight:900}
  .value-box{position:absolute;border:3px solid rgba(255,255,255,.9);border-radius:10px;
    background:linear-gradient(135deg,rgba(127,242,234,.25),rgba(0,118,114,.35));
    box-shadow:0 0 14px rgba(127,242,234,.5), 10px 0 0 -3px rgba(127,242,234,.25);
    display:flex;align-items:center;justify-content:center}
  .value-box svg{width:60%;height:60%;fill:none;stroke:var(--aqua);stroke-width:2.2;stroke-linecap:round;stroke-linejoin:round}
  .value-box .box-label{font-size:15px;font-weight:400;text-align:center;line-height:1.25;color:var(--white)}
  .value-label{position:absolute;font-size:23px;font-weight:400;line-height:1.3;text-transform:uppercase}
  .value-label.right-align{text-align:right}
  .phone{position:absolute;left:405px;top:368px;width:261px;height:392px;border-radius:30px;
    background:#1b1b1b;border:3px solid #555;padding:16px 10px 18px}
  .phone-screen{width:100%;height:100%;border-radius:6px;position:relative;overflow:hidden;
    background:linear-gradient(160deg,#0c9d96 0%,var(--teal) 60%,#0a938c 100%)}
  .phone-brand{position:absolute;top:74px;width:100%;text-align:center;font-size:32px;font-weight:700;letter-spacing:.06em}
  .phone-amount{position:absolute;left:27px;top:212px;width:187px;height:32px;background:var(--white);
    color:var(--ink);font-weight:900;font-size:25px;text-align:center;line-height:32px}
  .phone-pay{position:absolute;left:47px;top:270px;width:149px;height:62px;background:var(--lime);
    border-radius:4px;font-weight:900;font-size:44px;text-align:center;line-height:62px}
  .slogan{position:absolute;top:835px;left:0;width:100%;height:170px}
  .slogan-no{position:absolute;left:150px;top:0;font-weight:900;font-size:226px;line-height:170px;letter-spacing:-.02em}
  .slogan-cash{position:absolute;left:562px;top:4px;font-weight:900;font-size:118px;line-height:96px}
  .slogan-cash .dollar{color:var(--lime)}
  .slogan-worries{position:absolute;left:558px;top:104px;font-weight:900;font-size:80px;line-height:68px;letter-spacing:-.01em}
  .directions{position:absolute;top:1023px;left:0;width:100%;display:flex;align-items:center;justify-content:center;gap:16px;
    font-weight:700;font-size:28px}
  .directions::before,.directions::after{content:"";width:198px;height:4px;background:var(--aqua);border-radius:2px}
  .directions-line{position:absolute;top:1064px;width:100%;text-align:center;font-size:46px;font-weight:400}
  .directions-line b{font-weight:900}
  .site-url{position:absolute;top:1118px;width:100%;text-align:center;font-size:44px;font-weight:400;letter-spacing:.6em;padding-left:.6em}
</style>
</head>
<body>
<main class="poster">
  <svg class="rays" viewBox="0 0 1072 260" aria-hidden="true">
    <path d="M0 80 L470 190" stroke="rgba(200,255,250,.55)" stroke-width="5"/>
    <path d="M0 120 L470 200" stroke="rgba(200,255,250,.3)" stroke-width="3"/>
    <path d="M0 190 L470 205" stroke="rgba(255,190,190,.45)" stroke-width="3"/>
    <path d="M1072 70 L600 190" stroke="rgba(200,255,250,.6)" stroke-width="6"/>
    <path d="M1072 120 L600 200" stroke="rgba(200,255,250,.3)" stroke-width="3"/>
    <path d="M1072 200 L600 205" stroke="rgba(255,190,190,.45)" stroke-width="3"/>
  </svg>

  <header class="brand">
    <div class="brand-name">SWIFT</div>
    <div class="brand-rule"></div>
    <div class="brand-sub">TEE</div>
  </header>

  <h1 class="values-banner">OUR&nbsp;<b>KEY</b>&nbsp;VALUES</h1>

  <div class="value-box" style="left:220px;top:368px;width:148px;height:120px">
    <svg viewBox="0 0 48 48"><circle cx="26" cy="27" r="14"/><path d="M26 13v-4M22 9h8M26 27l6-5M6 22h8M4 28h8M6 34h8"/></svg>
  </div>
  <p class="value-label right-align" style="left:40px;top:404px;width:165px">Quick &amp;<br>Easy</p>

  <div class="value-box" style="left:147px;top:507px;width:113px;height:81px">
    <svg viewBox="0 0 48 48"><path d="M24 22c-6-4-8-8-5-11s5 0 5 2c0-2 2-5 5-2s1 7-5 11z"/><path d="M8 20v14l8 8M40 20v14l-8 8M12 24l6 8M36 24l-6 8"/></svg>
  </div>
  <p class="value-label" style="left:60px;top:598px;width:220px;text-align:center">Mate-ship<br>Relationships</p>

  <div class="value-box" style="left:265px;top:645px;width:127px;height:101px">
    <span class="box-label">ONLINE<br>PAYMENTS</span>
  </div>

  <div class="phone" role="img" aria-label="Mobile phone showing the Swift Tee payment screen">
    <div class="phone-screen">
      <div class="phone-brand">SWIFT TEE</div>
      <div class="phone-amount">$000</div>
      <div class="phone-pay">PAY</div>
    </div>
  </div>

  <div class="value-box" style="left:690px;top:368px;width:149px;height:110px">
    <svg viewBox="0 0 48 48"><path d="M4 20l10-8 8 4 6-3 8 3 8 6M10 22l12 12a3 3 0 0 0 4-4M18 30l6 6a3 3 0 0 0 4-4M24 26l6 6a3 3 0 0 0 4-4l-8-8"/></svg>
  </div>
  <p class="value-label" style="left:855px;top:412px;width:200px">Formal &amp;<br>Polite</p>

  <div class="value-box" style="left:809px;top:488px;width:120px;height:81px">
    <svg viewBox="0 0 48 48"><path d="M6 10h6l5 22h20l4-16H14M20 16v16M27 16v16M34 16v16"/><circle cx="19" cy="38" r="2.5"/><circle cx="35" cy="38" r="2.5"/></svg>
  </div>
  <p class="value-label" style="left:937px;top:558px">100%</p>
  <p class="value-label" style="left:810px;top:584px">Online Digital</p>

  <div class="value-box" style="left:694px;top:602px;width:133px;height:115px">
    <svg viewBox="0 0 48 48"><rect x="6" y="14" width="36" height="26" rx="3"/><path d="M18 14v-5h12v5M6 24h36M22 24v4h4v-4"/></svg>
  </div>
  <p class="value-label" style="left:840px;top:628px">Fun with<br>Professional<br>Boundary</p>

  <h2 class="slogan">
    <span class="slogan-no">NO</span>
    <span class="slogan-cash">CA<span class="dollar">$</span>H</span>
    <span class="slogan-worries">WORRIES</span>
  </h2>

  <footer>
    <p class="directions">DIRECTIONS</p>
    <p class="directions-line"><b>TO ONLINE PAYMENT</b> VIA</p>
    <p class="site-url">swifttee.com.au</p>
  </footer>
</main>
</body>
</html>
```